Our website, is loosely based on a grant proposal submitted to the Northfield Vascular Society last year for a community-based project that could improve the health of the community at large, I have attached this file for your review (underline "loosely). The idea is to create a "patient navigator" a website where patients can both learn and use as a resource for their care. I have been working on the project for some time, but my other responsibilities as a cardiologist have not allowed me time to learn and design a website of this type. Our website is intended for a spanish speaking audience and is in Spanish language. Designs in english will have to be translated. Our name: AcademiaBienestar.com: means a health university: One option is to have the website have a "university" theme. The project calls for: An initial: easy registration process: collecting name, DOB and city. Simplicity is key, many of our patients barely use computers, and this site is meant to make things easier, not complicate them. The web site should work as an extension of the doctors office, so it should be serious, creative, addictive, engaging. Doctors will see the patients in the office then refer them to the website to continue their learning about their conditions. There should be a page where patients can post questions: a panel of doctors: represented with their pictures, (in circles? around the question answered?) titles and small resumes (our "faculty") answers them. Every person that will attach themself to this website will have a title: doctors and nurses will be professors, residents and fellows will be assistant professors, aids can be PA?. The site should have a market place where people can purchase items that doctors recommend including foods, products and devices; here too, we can have a "bookshop". This should have a flexible mechanism for doctors to add their recommendations a patients can have access to them. Very important: there should be a site intended to be a classroom, this is the meat of this protect: where people can watch videos our staff will make to learn about different subjects; the site should keep track of the videos watched by the person and eventually "graduate them". These videos will be created by my staff, and added over time to the site, students should be able to "request" classes (videos). It should have a site where people can input their medications (notebook), have them stored and printed as a list if necessary. And finally it should have a contact and references section. We have set up a relationship with another site that help people count calories: and a link to this should be available. We have a link to our twitter account, This protect is intended to expand, and we hope to establish a long term relationship with the design team to expand it as needed in the future. The site is on PageHarbor and can be seen in its current form at AcademiaBienestar.com . We have had a logo designed with specific colors of the hospital I work with and one plan is to present it to our hospital to adopt our page in it final form. Again, this site is in spanish and intended for a spanish audience.

Target Market(s)

Spanish speaking, late 30s to early 60s audience.

Industry/Entity Type

Community

Number of Pages Required

4 page

Font styles to use
Sans Serif

Colors
a64599
fceff5
3277b5

Requirements
Must have
• A simple, accesible look
Nice to have
• Animations, moving parts
Should not have
• English

```html
<!DOCTYPE html>
<html lang="es">
<head>
<meta charset="utf-8">
<title>AcademiaBienestar</title>
<link href="https://fonts.googleapis.com/css2?family=Roboto:wght@300;400;500;700&display=swap" rel="stylesheet">
<style>
:root{
  --purple:#a64599;
  --pink:#fceff5;
  --blue:#3277b5;
  --navy:#234a75;
  --field:#244f80;
  --ink:#1f3a66;
  --text:#555;
  --grey:#8c8c8c;
  --line:#d9d9d9;
}
*{box-sizing:border-box;margin:0;padding:0}
html,body{width:1018px;height:1200px;overflow:hidden}
body{position:relative;font-family:'Roboto',sans-serif;background:#fff;color:var(--text)}
.abs{position:absolute}
.band-pink{background:var(--pink)}
.band-blue{background:var(--blue)}
.purple{background:var(--purple)}
.blue{background:var(--blue)}
.white{background:#fff}

/* header */
.site-header{left:0;top:0;width:1018px;height:96px}
.brand{left:146px;top:33px;font-size:24px;font-weight:300;color:var(--ink);letter-spacing:-.2px}
.nav{left:405px;top:42px;font-size:11px;color:#333}
.nav span{position:absolute;top:0;white-space:nowrap}
.nav .active{color:var(--purple)}
.social-mini{left:793px;top:42px;display:flex;gap:8px}
.social-mini i{width:12px;height:12px;border-radius:2px;background:#b9b9b9;display:block}

/* tiles */
.tile{color:#fff;display:flex;align-items:center;justify-content:center;text-align:center;border:1px solid rgba(255,255,255,.25)}
.tile .big{font-size:27px;font-weight:700;line-height:1}
.tile .cap{font-size:9px;font-weight:500;text-transform:uppercase}
.tile .small{font-size:9px;font-weight:500;line-height:1.15}
.pin{width:8px;height:10px;margin-right:3px}
.figure-slot{background:#e7e7ec;border-radius:4px}
.figure-slot.onc{background:rgba(255,255,255,.35)}
.label-row{display:flex;align-items:center;gap:10px;font-size:9px;font-weight:700;color:#fff;line-height:1.15}

/* sections */
.cta-text{font-size:19px;font-weight:400;color:var(--text);white-space:nowrap}
.btn-dark{background:var(--navy);color:#fff;font-size:14px;display:flex;align-items:center;justify-content:center;text-transform:uppercase}
.welcome-title{left:148px;top:588px;font-size:25px;font-weight:300;color:var(--ink)}
.welcome-title b{font-weight:300;color:var(--purple)}
.lorem{left:147px;top:624px;width:422px;font-size:9.6px;line-height:11.3px;color:#444}
.btn-read{left:146px;top:734px;width:102px;height:30px;background:var(--purple);color:#fff;font-size:9px;font-weight:500;display:flex;align-items:center;justify-content:center}

.quote-card{left:656px;top:572px;width:216px;height:211px;background:var(--blue);border:1px solid #2a64a0;border-radius:2px;color:#fff}
.quote-card h3{position:absolute;left:0;top:19px;width:100%;text-align:center;font-size:13px;font-weight:500}
.quote-card p{position:absolute;left:20px;top:38px;width:176px;text-align:center;font-size:9px;line-height:11px}
.field{position:absolute;left:17px;width:178px;height:24px;background:var(--field);font-size:9px;font-weight:500;padding:8px 12px 0}
.send{position:absolute;left:113px;top:166px;width:82px;height:26px;background:#fff;color:var(--blue);font-size:10px;font-weight:700;display:flex;align-items:center;justify-content:center}

.avatar{width:82px;height:82px;border-radius:50%;border:3px solid var(--purple)}
.story h4{font-size:9.5px;font-weight:700;color:var(--purple);text-transform:uppercase}
.story p{font-size:9.5px;line-height:11px;color:#555;margin-top:5px;width:250px}

.footer-brand{left:146px;top:1164px;font-size:12px;color:var(--grey)}
.social-foot{left:759px;top:1158px;display:flex;gap:6px}
.social-foot i{width:24px;height:24px;border-radius:50%;background:var(--grey);display:block}
</style>
</head>
<body>

<header class="abs site-header band-pink">
  <div class="abs brand">AcademiaBienestar</div>
  <nav class="abs nav">
    <span class="active" style="left:0">INICIO</span>
    <span style="left:57px">ACERCA</span>
    <span style="left:124px">TIENDA</span>
    <span style="left:188px">BLOG</span>
    <span style="left:241px">FAQ</span>
    <span style="left:288px">CONTACTO</span>
  </nav>
  <div class="abs social-mini"><i></i><i></i><i></i><i></i></div>
</header>

<!-- infographic grid -->
<div class="abs tile blue" style="left:0;top:97px;width:98px;height:91px;font-size:10px;font-weight:500">
  <svg class="pin" viewBox="0 0 8 10"><path d="M4 0a4 4 0 0 0-4 4c0 3 4 6 4 6s4-3 4-6a4 4 0 0 0-4-4z" fill="#fff"/><circle cx="4" cy="4" r="1.5" fill="#3277b5"/></svg>CLÍNICAS
</div>
<div class="abs tile purple" style="left:0;top:188px;width:98px;height:90px;font-size:10px;font-weight:500">
  <svg class="pin" viewBox="0 0 8 10"><path d="M4 0a4 4 0 0 0-4 4c0 3 4 6 4 6s4-3 4-6a4 4 0 0 0-4-4z" fill="#fff"/><circle cx="4" cy="4" r="1.5" fill="#a64599"/></svg>OFICINAS
</div>
<div class="abs white" style="left:98px;top:96px;width:274px;height:182px;border:1px solid var(--line)">
  <div class="abs" role="img" aria-label="Mapa del mundo con clínicas y oficinas marcadas" style="left:14px;top:16px;width:246px;height:140px;background:linear-gradient(135deg,#d4d4d4,#bdbdbd 60%,#d9d0dc);border-radius:6px"></div>
</div>

<div class="abs" style="left:372px;top:96px;width:211px;height:365px;border:1px solid #9a9a9a;background:#fff">
  <div class="abs blue" style="left:0;top:0;width:209px;height:48px"></div>
  <div class="abs figure-slot onc" role="img" aria-label="Icono de médico" style="left:95px;top:7px;width:18px;height:34px"></div>
  <div class="abs" style="left:80px;top:71px;font-size:23px;font-weight:700;color:var(--blue)">6</div>
  <div class="abs" style="left:105px;top:69px;width:1px;height:35px;background:#ccc"></div>
  <div class="abs" style="left:101px;top:65px;width:9px;height:9px;border-radius:50%;background:#ccc"></div>
  <div class="abs" style="left:101px;top:98px;width:9px;height:9px;border-radius:50%;background:#ccc"></div>
  <div class="abs" style="left:116px;top:79px;font-size:9px;font-weight:500;color:var(--blue)">CARDIÓLOGOS</div>
  <div class="abs" style="left:48px;top:125px;width:114px;height:114px;border-radius:50%;background:#cfcfcf;display:flex;align-items:center;justify-content:center;font-size:12px;font-weight:400;color:var(--ink)">AcademiaBienestar</div>
  <div class="abs" style="left:52px;top:264px;font-size:23px;font-weight:700;color:var(--purple)">350</div>
  <div class="abs" style="left:105px;top:258px;width:1px;height:35px;background:#ccc"></div>
  <div class="abs" style="left:101px;top:254px;width:9px;height:9px;border-radius:50%;background:#ccc"></div>
  <div class="abs" style="left:101px;top:287px;width:9px;height:9px;border-radius:50%;background:#ccc"></div>
  <div class="abs" style="left:116px;top:272px;font-size:9px;font-weight:500;color:var(--purple)">PACIENTES</div>
  <div class="abs purple" style="left:0;top:314px;width:209px;height:49px"></div>
  <div class="abs figure-slot onc" role="img" aria-label="Icono de paciente" style="left:95px;top:322px;width:18px;height:34px"></div>
</div>

<div class="abs tile purple" style="left:583px;top:97px;width:106px;height:92px">
  <div class="abs figure-slot onc" role="img" aria-label="Icono de cardiólogo" style="left:10px;top:14px;width:32px;height:64px"></div>
  <div class="abs" style="left:46px;top:16px;width:56px"><div class="big">6</div><div class="small" style="margin-top:4px">cardiólogos multilingües</div></div>
</div>
<div class="abs tile blue" style="left:689px;top:97px;width:105px;height:92px">
  <div class="abs figure-slot onc" role="img" aria-label="Icono de paciente" style="left:8px;top:14px;width:32px;height:64px"></div>
  <div class="abs" style="left:46px;top:26px;width:52px"><div class="big" style="font-size:25px">350</div><div class="small" style="margin-top:3px">Pacientes</div></div>
</div>
<div class="abs tile blue" style="left:583px;top:189px;width:211px;height:89px;justify-content:flex-start;padding-left:30px">
  <svg width="36" height="36" viewBox="0 0 36 36" fill="none" stroke="#fff" stroke-width="2"><rect x="6" y="7" width="26" height="25" rx="2"/><line x1="6" y1="14" x2="32" y2="14"/><line x1="13" y1="4" x2="13" y2="10"/><line x1="25" y1="4" x2="25" y2="10"/><path d="M11 19h4M17 19h4M23 19h4M11 24h4M17 24h4M23 24h4" /></svg>
  <span class="big" style="margin-left:12px">1</span><span class="small" style="margin-left:8px">VISITAS POR SEMANA</span>
</div>

<div class="abs white" style="left:794px;top:96px;width:112px;height:112px;border:1px solid var(--line)">
  <div class="abs figure-slot" role="img" aria-label="Grupo de personas" style="left:30px;top:22px;width:52px;height:76px"></div>
</div>
<div class="abs white" style="left:906px;top:96px;width:112px;height:112px;border:1px solid var(--line)">
  <div class="abs figure-slot" role="img" aria-label="Grupo de personas" style="left:28px;top:22px;width:52px;height:76px"></div>
</div>
<div class="abs tile purple" style="left:794px;top:208px;width:112px;height:70px;flex-direction:column"><div class="big">100</div><div class="cap" style="margin-top:4px">PERSONAS</div></div>
<div class="abs tile blue" style="left:906px;top:208px;width:112px;height:70px;flex-direction:column"><div class="big">100</div><div class="cap" style="margin-top:4px">DE GENTE</div></div>

<div class="abs white" style="left:0;top:278px;width:176px;height:183px">
  <div class="abs" role="img" aria-label="Filas de figuras de personas en azul y morado" style="left:8px;top:10px;width:160px;height:164px;background:linear-gradient(180deg,#c9d9ec 0%,#c9d9ec 25%,#e6c9e2 25%,#e6c9e2 50%,#c9d9ec 50%,#c9d9ec 75%,#e6c9e2 75%);border-radius:4px"></div>
</div>
<div class="abs tile blue" style="left:176px;top:278px;width:97px;height:92px"><span class="big" style="font-size:20px">33%</span></div>
<div class="abs tile purple" style="left:273px;top:278px;width:99px;height:92px"><span class="big" style="font-size:20px">75%</span></div>
<div class="abs tile purple" style="left:176px;top:370px;width:97px;height:91px"><span class="big" style="font-size:20px">45%</span></div>
<div class="abs tile blue" style="left:273px;top:370px;width:99px;height:91px"><span class="big" style="font-size:20px">55%</span></div>

<svg class="abs" style="left:583px;top:278px" width="263" height="133" viewBox="0 0 263 133">
  <rect x="0" y="0" width="263" height="133" fill="#fff" stroke="#d9d9d9"/>
  <g stroke="#e6e6e6" stroke-width="1">
    <line x1="10" y1="20" x2="245" y2="20"/><line x1="10" y1="50" x2="245" y2="50"/><line x1="10" y1="80" x2="245" y2="80"/><line x1="10" y1="110" x2="245" y2="110"/>
    <line x1="50" y1="15" x2="50" y2="125"/><line x1="100" y1="15" x2="100" y2="125"/><line x1="150" y1="15" x2="150" y2="125"/><line x1="200" y1="15" x2="200" y2="125"/><line x1="245" y1="15" x2="245" y2="125"/>
  </g>
  <polyline points="11,95 103,66 143,90 180,53 198,65 240,24" fill="none" stroke="#3277b5" stroke-width="2"/>
  <polyline points="11,95 45,77 89,95 141,58 209,87 241,45" fill="none" stroke="#a64599" stroke-width="2"/>
  <g fill="#fff" stroke="#3277b5" stroke-width="2"><circle cx="103" cy="66" r="4"/><circle cx="143" cy="90" r="4"/><circle cx="180" cy="53" r="4"/><circle cx="198" cy="65" r="4"/><circle cx="240" cy="24" r="4"/></g>
  <g fill="#fff" stroke="#a64599" stroke-width="2"><circle cx="45" cy="77" r="4"/><circle cx="89" cy="95" r="4"/><circle cx="141" cy="58" r="4"/><circle cx="209" cy="87" r="4"/><circle cx="241" cy="45" r="4"/></g>
</svg>
<div class="abs blue label-row" style="left:583px;top:411px;width:131px;height:50px;padding-left:16px;gap:8px">
  <svg width="28" height="22" viewBox="0 0 28 22" fill="none" stroke="#fff" stroke-width="2" style="flex:none"><path d="M14 20S2 13 2 7a5 5 0 0 1 12-2 5 5 0 0 1 12 2c0 6-12 13-12 13z"/><polyline points="3,11 9,11 11,7 14,15 16,11 25,11"/></svg><span>Atención Médica</span>
</div>
<div class="abs purple label-row" style="left:714px;top:411px;width:132px;height:50px;padding-left:10px;gap:8px">
  <svg width="36" height="22" viewBox="0 0 36 22" fill="none" stroke="#fff" stroke-width="2" style="flex:none"><polygon points="18,2 34,8 18,14 2,8"/><path d="M8 11v6c6 4 14 4 20 0v-6"/></svg><span>Educación en Salud</span>
</div>
<div class="abs blue label-row" style="left:846px;top:278px;width:172px;height:62px;padding-left:12px">
  <svg width="46" height="26" viewBox="0 0 46 26" fill="#fff" style="flex:none"><circle cx="9" cy="10" r="7"/><rect x="19" y="6" width="26" height="14" rx="3"/><circle cx="26" cy="13" r="1.5" fill="#3277b5"/><circle cx="32" cy="13" r="1.5" fill="#3277b5"/><circle cx="38" cy="13" r="1.5" fill="#3277b5"/></svg><span>Comprensión del Inglés</span>
</div>
<div class="abs purple label-row" style="left:846px;top:340px;width:172px;height:61px;padding-left:12px">
  <svg width="46" height="26" viewBox="0 0 46 26" fill="none" stroke="#fff" stroke-width="2" style="flex:none"><path d="M4 8v15c6-2 12-2 19 1 7-3 13-3 19-1V8"/><path d="M8 6v14c5-1 10 0 15 3 5-3 10-4 15-3V6c-5-1-10 0-15 3-5-3-10-4-15-3z"/><line x1="23" y1="9" x2="23" y2="23"/></svg><span>Sesgos Culturales</span>
</div>
<div class="abs blue label-row" style="left:846px;top:401px;width:172px;height:60px;padding-left:12px">
  <svg width="46" height="28" viewBox="0 0 46 28" fill="#fff" style="flex:none"><rect x="3" y="18" width="4" height="9"/><rect x="9" y="14" width="4" height="13"/><rect x="15" y="10" width="4" height="17"/><rect x="21" y="6" width="4" height="21"/><path d="M2 14 L20 3 l-2-3 h9 v8 l-3-2 L4 17z"/></svg><span>Nivel Socioeconómico</span>
</div>

<!-- call to action -->
<section class="abs band-pink" style="left:0;top:461px;width:1018px;height:82px">
  <div class="abs cta-text" style="left:148px;top:29px">¡CONTÁCTENOS AHORA Y MEJORE SU SALUD!</div>
  <div class="abs btn-dark" style="left:639px;top:19px;width:233px;height:43px">PIDA SU CITA AHORA</div>
</section>

<!-- welcome -->
<h1 class="abs welcome-title">Bienvenido a <b>AcademiaBienestar</b></h1>
<p class="abs lorem">Lorem ipsum dolor sit amet, consectetuer adipiscing elit, sed diam nonummy nibhdf euismod tincidunt ut laoreet dolore magna aliquam erat volutpat. Ut wisi enim adsdv minim veniam, quis nostrud exerci tation ullamcorper suscipit lobortis nisl ut aliquips ex ea commodo consequat. autem vel eum iriure dolor in hendrerit in vulputate velitLorem ipsum dolor sit amet, consectetuer adipiscing elit, sed diam nonummy nibhdf euismod tincidunt ut laoreet dolore magna aliquam erat volutpat. Ut wisi enim adsdv minim veniam, quis nostrud exerci tation ullamcorper suscipit lobortis nisl ut aliquips ex ea commodo consequat. autem vel eum iriure dolor in hendrerit in vulputate velitLorem ipsum dolor sit amet, consectetuer adipiscing elit, sed diam nonummy nibhdf euismod tincidunt ut laoreet dolore magna aliquam erat volutpat. Ut wisi enim adsdv minim veniam, quis</p>
<div class="abs btn-read">LEER MÁS</div>

<form class="abs quote-card">
  <h3>¡Obtenga ahora un Presupuesto!</h3>
  <p>Lorem ipsum dolor sit amet, consectetuer adipiscing</p>
  <div class="field" style="top:72px">NOMBRE</div>
  <div class="field" style="top:102px">CORREO</div>
  <div class="field" style="top:133px">FECHA DE NACIMIENTO</div>
  <div class="abs" style="left:17px;top:174px;font-size:9px;font-weight:500">CONTACTO</div>
  <div class="send">ENVIAR</div>
</form>

<!-- faculty stories -->
<section class="abs band-pink" style="left:0;top:810px;width:1018px;height:244px">
  <div class="abs avatar" role="img" aria-label="Foto de mujer joven leyendo" style="left:147px;top:29px;background:linear-gradient(135deg,#d9b48c,#8a6a4a)"></div>
  <div class="abs story" style="left:239px;top:52px"><h4>Lorem ipsum dolor sit amet, ?</h4><p>Lorem ipsum dolor sit amet, consectetuer adipiscing elit, diam nonummy nibhdf euismod tincidunt ut laoreet dolore.</p></div>
  <div class="abs avatar" role="img" aria-label="Foto de hombre sonriente con tableta" style="left:535px;top:29px;background:linear-gradient(135deg,#8fb6cf,#3f6f91)"></div>
  <div class="abs story" style="left:628px;top:52px"><h4>Lorem ipsum dolor sit amet, ?</h4><p>Lorem ipsum dolor sit amet, consectetuer adipiscing elit, diam nonummy nibhdf euismod tincidunt ut laoreet dolore.</p></div>
  <div class="abs avatar" role="img" aria-label="Foto de mujer estudiando" style="left:147px;top:131px;background:linear-gradient(135deg,#b5765c,#4d5f6e)"></div>
  <div class="abs story" style="left:239px;top:154px"><h4>Lorem ipsum dolor sit amet, ?</h4><p>Lorem ipsum dolor sit amet, consectetuer adipiscing elit, diam nonummy nibhdf euismod tincidunt ut laoreet dolore.</p></div>
  <div class="abs avatar" role="img" aria-label="Foto de hombre con tableta" style="left:535px;top:131px;background:linear-gradient(135deg,#a9cde6,#5d8fb5)"></div>
  <div class="abs story" style="left:628px;top:154px"><h4>Lorem ipsum dolor sit amet, ?</h4><p>Lorem ipsum dolor sit amet, consectetuer adipiscing elit, diam nonummy nibhdf euismod tincidunt ut laoreet dolore.</p></div>
</section>

<!-- classes band -->
<section class="abs band-blue" style="left:0;top:1054px;width:1018px;height:83px;background:#3172b0">
  <div class="abs cta-text" style="left:146px;top:30px;color:#fff">¡PARA APRENDER, SOLICITE CLASES EN VIDEO!</div>
  <div class="abs btn-dark" style="left:639px;top:21px;width:233px;height:42px">SOLICITAR CLASES</div>
</section>

<footer>
  <div class="abs footer-brand">Derechos reservados © 2014 AcademiaBienestar</div>
  <div class="abs social-foot"><i></i><i></i><i></i><i></i></div>
</footer>

</body>
</html>
```